Verpackungsdesign für Kaffeefilter
Sehr gute Kommunikation! Schnelle und zuverlässige Bearbeitung! Klasse, gerne wieder.
Zielgruppe
Wir, TERAL GmbH, sind größter Hersteller von privat label Kaffeefiltern. Für unsere Eigenmarke LIVA Premium Kaffeefilter Größe 4, 80 Stück, braun wird ein kreatives und frisches Verpackungsdesign benötigt. Zielgruppe für die LIVA Premium Kaffeefilter sind internationale Filterkaffeetrinker im Altersspektrum 18 bis 50 Jahre.
Aufgabenstellung
Wir wünschen uns ein Faltschachtel - Design, welches frisch und jugendlich, luxuriös / hochwertig aber nicht opulent/barock, smart und reduziert (nicht überladen), nicht verspielt, abstrakt und schematisch sowie skandinavisch und modern, für einen internationalen Kundenkreis, ist. Die gesamte Faltschachtel (beiliegende Stanze) soll gestaltet werden.
Es sollen weder eine fotografische Filterabbildung noch andere Fotos auf der Verpackung sein.
WPQ Logo und Grüner Falke sowie Herstelleradresse und 3 Barcodefelder werden benötigt.
ACHTUNG: Die Aufreißlasche ist die Rückseite! Die Front steht im Tray. Es wird ca. 25% im unteren Teil der Faltschachtel vom Tray verdeckt.

```html
<!DOCTYPE html>
<html lang="de">
<head>
<meta charset="utf-8">
<title>LIVA Premium Kaffeefilter – Faltschachtel Front</title>
<link rel="stylesheet" href="https://fonts.googleapis.com/css2?family=Libre+Baskerville&family=Josefin+Sans:wght@300;400&display=swap">
<style>
  :root {
    --bg: #ececec;
    --box: #6d716f;
    --label: #f7f7f5;
    --ink: #555555;
    --rule: #6a6a6a;
    --kraft: #c9b08c;
    --stone: #a3a6a6;
    --charcoal: #4d4d4d;
    --cream: #e8e4dc;
    --badge: #f2f1ee;
  }
  * { margin: 0; padding: 0; box-sizing: border-box; }
  html, body { width: 1200px; height: 1200px; overflow: hidden; background: var(--bg); }
  .carton {
    position: absolute; left: 210px; top: 40px;
    width: 780px; height: 1120px;
    background: var(--box);
  }
  .label {
    position: absolute; left: 110px; top: 0;
    width: 560px; height: 450px;
  }
  .label-shape { position: absolute; inset: 0; }
  .brand {
    position: absolute; left: 50px; top: 120px;
    display: flex; align-items: flex-end; gap: 22px;
  }
  .brand-name {
    font-family: "Libre Baskerville", serif;
    font-size: 64px; letter-spacing: 14px; color: var(--ink); line-height: 1;
  }
  .brand-sub {
    font-family: "Libre Baskerville", serif;
    font-size: 15px; letter-spacing: 5px; color: var(--ink); line-height: 1.6;
    padding-bottom: 8px;
  }
  .spec-table {
    position: absolute; left: 40px; top: 240px; width: 490px;
    border-collapse: collapse; table-layout: fixed;
    font-family: "Josefin Sans", sans-serif; font-weight: 300;
    font-size: 20px; letter-spacing: 4px; color: var(--ink);
    white-space: nowrap;
  }
  .spec-table td {
    border-top: 2px solid var(--rule); border-bottom: 2px solid var(--rule);
    height: 78px; padding: 4px 0 0 14px; vertical-align: middle;
  }
  .spec-table td + td { border-left: 2px solid var(--rule); }
  .spec-table .icon-cell { padding: 0; }
  .filter-mark {
    display: block; width: 70px; height: 34px; margin: 0 auto;
    background: var(--kraft); opacity: .55;
    clip-path: polygon(0 0, 100% 0, 80% 100%, 20% 100%);
  }
  .pattern-band {
    position: absolute; left: 0; top: 650px; width: 100%; height: 250px;
    background: linear-gradient(90deg, var(--stone), var(--kraft) 25%, var(--charcoal) 45%, var(--cream) 60%, var(--stone) 80%, var(--kraft));
  }
  .certs {
    position: absolute; left: 0; top: 960px; width: 100%; height: 100px;
    display: flex; align-items: center; justify-content: center; gap: 50px;
  }
  .seal-badge { width: 90px; height: 90px; border-radius: 50%; background: var(--badge); }
  .eco-note {
    background: var(--badge); border-radius: 6px; padding: 10px 14px;
    font-family: "Josefin Sans", sans-serif; color: var(--ink);
    width: 240px;
  }
  .eco-note strong { font-weight: 400; font-size: 14px; display: block; margin-bottom: 4px; }
  .eco-note ul { list-style: none; font-size: 11px; line-height: 1.5; font-weight: 300; }
  .cert-badge { width: 200px; height: 86px; background: var(--badge); border-radius: 6px; }
</style>
</head>
<body>
  <div class="carton">
    <div class="label">
      <svg class="label-shape" viewBox="0 0 560 450" width="560" height="450" aria-hidden="true">
        <polygon fill="var(--label)" points="0,0 560,0 560,430 546,438 532,430 518,438 504,430 490,438 476,430 462,438 448,430 434,438 420,430 406,438 392,430 378,438 364,430 350,438 336,430 322,438 308,430 294,438 280,430 266,438 252,430 238,438 224,430 210,438 196,430 182,438 168,430 154,438 140,430 126,438 112,430 98,438 84,430 70,438 56,430 42,438 28,430 14,438 0,430"/>
      </svg>
      <div class="brand">
        <span class="brand-name">LIVA</span>
        <span class="brand-sub">PREMIUM<br>KAFFEEFILTER</span>
      </div>
      <table class="spec-table">
        <colgroup><col style="width:34%"><col style="width:27%"><col></colgroup>
        <tr>
          <td>80 STÜCK</td>
          <td class="icon-cell"><span class="filter-mark" role="img" aria-label="Schematische Darstellung eines Kaffeefilters"></span></td>
          <td>GRÖßE 4</td>
        </tr>
        <tr>
          <td>BRAUN</td>
          <td colspan="2">UMWELTFREUNDLICH</td>
        </tr>
      </table>
    </div>

    <div class="pattern-band" role="img" aria-label="Geometrisches Muster aus Viertelkreisen und Dreiecken in Grau, Kraftbraun, Anthrazit und Creme"></div>

    <div class="certs">
      <div class="seal-badge" role="img" aria-label="Platz für das Umweltsiegel Grüner Falke"></div>
      <div class="eco-note">
        <strong>www.gruener-falke.de</strong>
        <ul>
          <li>gewässerschonend hergestellt</li>
          <li>Holzfasern aus nachhaltiger Forstwirtschaft</li>
          <li>ungebleicht</li>
        </ul>
      </div>
      <div class="cert-badge" role="img" aria-label="Platz für das WPQ-Zertifikat"></div>
    </div>
  </div>
</body>
</html>
```